Business cards for Remote DBA team

Business cards for team offering database administration, consultation, machine learning and AI services. As of now team is using both
www.korvilnet.cz and www.brestmoorlab.cz URLs

Target Market(s)

IT managers

Industry/Entity Type

It Professional

Contact Information for Business Card

Should include logo
name, email, phone, twitter tag

Font styles to use
Sans Serif

Colors

Designer to choose colors to be used in the design.

```html
<!DOCTYPE html>
<html lang="en">
<head>
<meta charset="utf-8">
<title>Korvil Lab — Business Cards</title>
<link rel="stylesheet" href="https://fonts.googleapis.com/css2?family=Montserrat:wght@400;500;600;800&display=swap">
<style>
  :root {
    --bg: #2b2c2f;
    --card-white: #ffffff;
    --brand-blue: #0f8fd0;
    --deep-blue: #1477bd;
    --light-blue: #cfe6f6;
    --grey: #8a8c8e;
    --ink-white: #ffffff;
    --img-navy: #1b2a6b;
    --img-violet: #6a5fd0;
    --img-cyan: #58c3ee;
    --img-pink: #e2529a;
  }
  * { box-sizing: border-box; margin: 0; padding: 0; }
  html, body { width: 1200px; height: 900px; overflow: hidden; }
  body {
    background: var(--bg);
    font-family: "Montserrat", sans-serif;
    position: relative;
  }
  .card {
    position: absolute;
    left: 240px;
    width: 720px;
    height: 400px;
    border-radius: 26px;
    overflow: hidden;
    box-shadow: 0 14px 30px rgba(0,0,0,.45);
  }
  .card-front { top: 40px; background: var(--card-white); display: flex; align-items: center; justify-content: center; }
  .card-back  { top: 470px; background: linear-gradient(180deg, var(--card-white) 0%, var(--light-blue) 38%, var(--brand-blue) 78%, var(--deep-blue) 100%); }

  .brand { display: flex; align-items: center; gap: 16px; }
  .brand-dot { width: 46px; height: 46px; border-radius: 50%; background: var(--brand-blue); flex: none; }
  .brand-name {
    font-weight: 800; color: var(--brand-blue); letter-spacing: .5px;
    font-size: 50px; line-height: 1;
  }
  .card-back .brand { position: absolute; left: 40px; top: 42px; }
  .card-back .brand-dot { width: 34px; height: 34px; }
  .card-back .brand-name { font-size: 38px; }

  .hero-image {
    position: absolute; right: 0; top: 0; width: 62%; height: 100%;
    background:
      radial-gradient(circle at 62% 45%, var(--img-cyan) 0%, rgba(88,195,238,.35) 22%, transparent 45%),
      radial-gradient(circle at 40% 70%, rgba(226,82,154,.55) 0%, transparent 40%),
      linear-gradient(120deg, var(--img-violet) 0%, var(--img-navy) 55%, #2a3f9a 100%);
    -webkit-mask-image: linear-gradient(90deg, transparent 0%, #000 22%);
            mask-image: linear-gradient(90deg, transparent 0%, #000 22%);
  }

  .person { position: absolute; left: 40px; top: 170px; color: var(--ink-white); }
  .person-name { font-weight: 800; font-size: 30px; letter-spacing: .5px; text-transform: uppercase; }
  .person-role { font-weight: 600; font-size: 16px; letter-spacing: 1px; text-transform: uppercase; margin-top: 2px; }

  .contact-list { position: absolute; left: 40px; top: 244px; list-style: none; color: var(--ink-white); }
  .contact-item { display: flex; align-items: center; gap: 12px; font-size: 19px; font-weight: 500; height: 29px; letter-spacing: .3px; }
  .contact-icon { width: 22px; height: 22px; flex: none; }
</style>
</head>
<body>

<section class="card card-front">
  <div class="brand">
    <span class="brand-dot"></span>
    <span class="brand-name">KORVIL LAB</span>
  </div>
</section>

<section class="card card-back">
  <div class="hero-image" role="img" aria-label="Digital globe with glowing network nodes, data icons and binary digits in blue and pink light"></div>

  <div class="brand">
    <span class="brand-dot"></span>
    <span class="brand-name">KORVIL LAB</span>
  </div>

  <div class="person">
    <p class="person-name">Lukas Borovy</p>
    <p class="person-role">Data Platform Architect</p>
  </div>

  <ul class="contact-list">
    <li class="contact-item">
      <svg class="contact-icon" viewBox="0 0 24 24" fill="none" stroke="#fff" stroke-width="1.6"><circle cx="12" cy="12" r="10.5"/><path d="M8.5 7.5l2 2-1.2 1.5a7 7 0 0 0 3.7 3.7l1.5-1.2 2 2-1.3 1.3c-3.5 0-8-4.5-8-8z"/></svg>
      0712-4418-3096
    </li>
    <li class="contact-item">
      <svg class="contact-icon" viewBox="0 0 24 24" fill="none" stroke="#fff" stroke-width="1.6"><circle cx="12" cy="12" r="10.5"/><rect x="6.5" y="8" width="11" height="8"/><path d="M6.5 8l5.5 4.5L17.5 8"/></svg>
      lukas@brestmoorlab.cz
    </li>
    <li class="contact-item">
      <svg class="contact-icon" viewBox="0 0 24 24" fill="none" stroke="#fff" stroke-width="1.6"><circle cx="12" cy="12" r="10.5"/></svg>
      @korvillab
    </li>
    <li class="contact-item">
      <svg class="contact-icon" viewBox="0 0 24 24" fill="none" stroke="#fff" stroke-width="1.4"><circle cx="12" cy="12" r="10.5"/><circle cx="12" cy="12" r="6.5"/><path d="M5.5 12h13M12 5.5c-3 3.5-3 9.5 0 13M12 5.5c3 3.5 3 9.5 0 13"/></svg>
      www.korvilnet.cz
    </li>
    <li class="contact-item">
      <svg class="contact-icon" viewBox="0 0 24 24" fill="none" stroke="#fff" stroke-width="1.4"><circle cx="12" cy="12" r="10.5"/><circle cx="12" cy="12" r="6.5"/><path d="M5.5 12h13M12 5.5c-3 3.5-3 9.5 0 13M12 5.5c3 3.5 3 9.5 0 13"/></svg>
      www.brestmoorlab.cz
    </li>
  </ul>
</section>

</body>
</html>
```